Young and modern Electrical company working in the commercial arena.

Wanting a business card design thats modern and will last. Maybe Minimalist? Happy to look at changing my logo

Target Market(s)

Builders, Project Managers

Industry/Entity Type

Electrical

Contact Information for Business Card

Name
Address
Phone number
Job title

Logo Text

our name or just the logo i'm open to ideas

Font styles to use
Sans Serif

Requirements
Nice to have
• would like to keep the purple in our current logo. it's kinda unique to our market
Should not have
• Don't want it to be to busy. simple is best i think

```html
<!DOCTYPE html>
<html lang="en">
<head>
<meta charset="UTF-8">
<title>Halvern Electrical – Business Card</title>
<link rel="stylesheet" href="https://fonts.googleapis.com/css2?family=Lato:wght@400;700&family=Josefin+Sans:wght@400;600&display=swap">
<style>
  :root {
    --bg: #2b2b2c;
    --card: #1d1d1f;
    --purple: #7b4fc4;
    --purple-soft: #8e63d6;
    --white: #f4f4f6;
    --muted: #d9d9de;
  }
  * { margin: 0; padding: 0; box-sizing: border-box; }
  html, body { width: 1200px; height: 900px; overflow: hidden; }
  body {
    background: var(--bg);
    font-family: "Lato", Arial, sans-serif;
    color: var(--white);
    position: relative;
  }
  .card {
    position: absolute;
    left: 250px;
    width: 700px;
    height: 400px;
    background: linear-gradient(160deg, #242427 0%, var(--card) 60%, #19191b 100%);
    box-shadow: 0 14px 30px rgba(0,0,0,.45);
    overflow: hidden;
  }
  .card::after {
    content: "";
    position: absolute;
    left: 0; right: 0; bottom: 0;
    height: 7px;
    background: var(--purple);
  }
  .card--front { top: 30px; }
  .card--back { top: 470px; }

  .wordmark {
    display: flex;
    align-items: center;
    gap: 12px;
    color: var(--purple-soft);
    font-family: "Lato", Arial, sans-serif;
    font-weight: 700;
    letter-spacing: .5px;
    white-space: nowrap;
  }
  .wordmark__dot {
    width: 14px; height: 14px;
    background: var(--purple-soft);
  }
  .card--front .wordmark {
    position: absolute;
    left: 50%; top: 50%;
    transform: translate(-50%, -50%);
    font-size: 44px;
  }
  .card--back .wordmark {
    position: absolute;
    left: 48px; top: 170px;
    font-size: 30px;
  }
  .card--back .wordmark__dot { width: 11px; height: 11px; }

  .divider {
    position: absolute;
    left: 352px; top: 90px;
    width: 2px; height: 200px;
    background: var(--white);
  }
  .details {
    position: absolute;
    left: 376px; top: 86px;
    width: 300px;
  }
  .details__name {
    font-family: "Josefin Sans", Arial, sans-serif;
    font-weight: 600;
    font-size: 28px;
    letter-spacing: 2px;
    color: var(--purple-soft);
    text-transform: uppercase;
    line-height: 1;
  }
  .details__title {
    font-size: 16px;
    color: var(--muted);
    margin: 4px 0 16px;
  }
  .details__address {
    font-size: 16px;
    line-height: 1.3;
    color: var(--muted);
    margin-bottom: 12px;
  }
  .contact { list-style: none; }
  .contact__item {
    display: flex;
    align-items: center;
    gap: 10px;
    font-size: 16px;
    line-height: 24px;
    color: var(--white);
  }
  .contact__icon { width: 12px; height: 12px; flex: none; }
  .contact__accent { color: var(--purple-soft); }
</style>
</head>
<body>
  <section class="card card--front" aria-label="Card front">
    <div class="wordmark"><span class="wordmark__dot"></span>halvern electrical</div>
  </section>

  <section class="card card--back" aria-label="Card back">
    <div class="wordmark"><span class="wordmark__dot"></span>halvern electrical</div>
    <div class="divider"></div>
    <div class="details">
      <h1 class="details__name">Daniel Price</h1>
      <p class="details__title">Director</p>
      <p class="details__address">Harbour Lane,<br>Marrick NSW, Australia</p>
      <ul class="contact">
        <li class="contact__item">
          <svg class="contact__icon" viewBox="0 0 12 12"><path d="M2.5 1h2l1 2.5-1.3 1a6 6 0 0 0 3.3 3.3l1-1.3L11 7.5v2a1 1 0 0 1-1 1A9 9 0 0 1 1.5 2a1 1 0 0 1 1-1z" fill="#8e63d6"/></svg>
          0400123456
        </li>
        <li class="contact__item">
          <svg class="contact__icon" viewBox="0 0 12 12"><rect x="3" y="0.5" width="6" height="11" rx="1.2" fill="none" stroke="#8e63d6" stroke-width="1.2"/><circle cx="6" cy="9.6" r=".7" fill="#8e63d6"/></svg>
          0411987654
        </li>
        <li class="contact__item">
          <svg class="contact__icon" viewBox="0 0 12 12"><rect x="0.8" y="2.5" width="10.4" height="7" fill="none" stroke="#8e63d6" stroke-width="1.1"/><path d="M1 3l5 3.6L11 3" fill="none" stroke="#8e63d6" stroke-width="1.1"/></svg>
          admin@halvernelectrical.com.au
        </li>
        <li class="contact__item">
          <svg class="contact__icon" viewBox="0 0 12 12"><circle cx="6" cy="6" r="5.3" fill="none" stroke="#8e63d6" stroke-width="1.1"/><ellipse cx="6" cy="6" rx="2.3" ry="5.3" fill="none" stroke="#8e63d6" stroke-width="1"/><path d="M.8 6h10.4" stroke="#8e63d6" stroke-width="1"/></svg>
          <span>www.<span class="contact__accent">halvernelectrical</span>.com.au</span>
        </li>
      </ul>
    </div>
  </section>
</body>
</html>
```